Qivora IT Company Business Card

📌 Objective:
Create a modern, fluid and stylish business card that reflects the identity of our IT company and our partnership with Veltrana.
📍 Key information:
• Company name: Qivora
• Activity: Veltrana 720 Expert
• Colors to favor: Inspired by the Qivora logo
• Style: Minimalist, modern, professional
• Front / Back:
• Items to include:
o Company logo
o Name and surname
o Post
o Email
o Phone
o Website
o QR code (optional)
🎨 Inspirations & Expectations:
• Sleek design with a high-tech touch
• Possibly subtle graphic elements linked to the Veltrana universe
• Good readability and balance between text and visuals

Lent pour commenter

Target Market(s)

Private, public

Contact Information for Business Card

Veltrana720, Formation, Gouvernance, Migration, Sécurité

Colors
6B429C
8869AF
B7A5CE
E3DAEB
F3F0F8

Requirements
Nice to have
• Have the icons of the applications I work on

```html
<!DOCTYPE html>
<html lang="en">
<head>
<meta charset="utf-8">
<title>Qivora Business Card</title>
<link rel="stylesheet" href="https://fonts.googleapis.com/css2?family=Lato:wght@400;700;900&display=swap">
<style>
  :root {
    --backdrop: #2c2c2c;
    --purple-deep: #6b429c;
    --purple-mid: #8869af;
    --purple-soft: #b7a5ce;
    --lilac: #e6dcec;
    --divider: #a996c6;
    --ink: #111111;
    --ink-soft: #222222;
    --accent-red: #e8455e;
    --icon-teal: #2a9fc4;
    --app-blue: #2f6fd6;
    --app-indigo: #5059c9;
    --app-teal: #0b7f7a;
    --app-navy: #0e5fb3;
    --app-violet: #a45ad8;
  }
  * { box-sizing: border-box; margin: 0; padding: 0; }
  html, body { width: 1200px; height: 1000px; overflow: hidden; }
  body {
    background: var(--backdrop);
    font-family: "Lato", sans-serif;
    position: relative;
  }
  .card {
    position: absolute;
    left: 205px;
    width: 790px;
    height: 462px;
    border-radius: 40px;
    overflow: hidden;
  }
  .card-front {
    top: 30px;
    background: radial-gradient(circle at 16% 43%, var(--purple-soft) 0%, var(--purple-mid) 38%, var(--purple-deep) 75%);
  }
  .front-pattern {
    position: absolute;
    inset: 0;
    background: radial-gradient(circle at 16% 43%, rgba(255,255,255,0.08), rgba(255,255,255,0) 60%);
  }
  .front-wordmark {
    position: absolute;
    left: 485px;
    top: 322px;
    display: flex;
    align-items: center;
    gap: 12px;
    font-weight: 900;
    font-size: 46px;
    color: #ffffff;
    letter-spacing: -0.5px;
  }
  .front-wordmark .mark-dot {
    width: 22px; height: 22px; border-radius: 50%;
    background: #ffffff;
  }
  .card-back {
    top: 510px;
    background: var(--lilac);
  }
  .brand-block {
    position: absolute;
    left: 50px;
    top: 140px;
    width: 320px;
    text-align: center;
  }
  .brand-name {
    display: inline-flex;
    align-items: center;
    gap: 12px;
    font-weight: 900;
    font-size: 50px;
    color: var(--ink);
    letter-spacing: -1px;
  }
  .brand-name .mark-dot {
    width: 22px; height: 22px; border-radius: 50%;
    background: var(--ink);
  }
  .app-row {
    display: flex;
    justify-content: center;
    gap: 20px;
    margin-top: 26px;
  }
  .app-badge {
    width: 40px; height: 40px; border-radius: 9px;
  }
  .app-badge.flow { background: var(--app-blue); }
  .app-badge.chat { background: var(--app-indigo); }
  .app-badge.share { background: var(--app-teal); }
  .app-badge.mail { background: var(--app-navy); }
  .app-badge.assist { background: linear-gradient(135deg, #f07b3f, var(--app-violet), #2fb6e8); }
  .divider {
    position: absolute;
    left: 395px;
    top: 138px;
    width: 1.5px;
    height: 215px;
    background: var(--divider);
  }
  .person {
    position: absolute;
    left: 458px;
    top: 146px;
  }
  .person-name {
    font-weight: 900;
    font-size: 36px;
    color: var(--accent-red);
    letter-spacing: 0.3px;
    line-height: 1;
  }
  .person-title {
    margin-top: 10px;
    margin-left: 2px;
    font-weight: 700;
    font-size: 20px;
    color: var(--ink-soft);
  }
  .contact-list {
    list-style: none;
    margin-top: 34px;
    margin-left: 2px;
  }
  .contact-list li {
    display: flex;
    align-items: center;
    gap: 10px;
    font-size: 21px;
    color: var(--ink-soft);
    height: 34px;
    letter-spacing: 0.2px;
  }
  .contact-icon {
    width: 24px; height: 24px;
    flex: none;
  }
</style>
</head>
<body>

<section class="card card-front">
  <div class="front-pattern" role="img" aria-label="Repeating embossed brand pattern on purple"></div>
  <div class="front-wordmark"><span class="mark-dot"></span>Qivora</div>
</section>

<section class="card card-back">
  <div class="brand-block">
    <div class="brand-name"><span class="mark-dot"></span>Qivora</div>
    <div class="app-row">
      <span class="app-badge flow" aria-hidden="true"></span>
      <span class="app-badge chat" aria-hidden="true"></span>
      <span class="app-badge share" aria-hidden="true"></span>
      <span class="app-badge mail" aria-hidden="true"></span>
      <span class="app-badge assist" aria-hidden="true"></span>
    </div>
  </div>

  <div class="divider"></div>

  <div class="person">
    <h1 class="person-name">DARA VELKIN</h1>
    <p class="person-title">Vice President</p>
    <ul class="contact-list">
      <li>
        <svg class="contact-icon" viewBox="0 0 24 24" fill="none" stroke="var(--icon-teal)" stroke-width="1.6">
          <rect x="1.5" y="1.5" width="21" height="21" rx="3"/>
          <path d="M8 6.5l2 2.5-1.2 1.5c.8 1.7 2 2.9 3.7 3.7L14 13l2.5 2-1 2c-4.5-.3-8.2-4-8.5-8.5z" stroke-linejoin="round"/>
        </svg>
        <span>044-555 018 274</span>
      </li>
      <li>
        <svg class="contact-icon" viewBox="0 0 24 24" fill="none" stroke="var(--icon-teal)" stroke-width="1.6">
          <rect x="1.5" y="1.5" width="21" height="21" rx="3"/>
          <path d="M5.5 11.5L18 6.5l-2.3 11-4-3-2 2v-3.2l6-5.3-7.2 4.5z" stroke-linejoin="round"/>
        </svg>
        <span>hello@qivora.com</span>
      </li>
      <li>
        <svg class="contact-icon" viewBox="0 0 24 24" fill="none" stroke="var(--icon-teal)" stroke-width="1.6">
          <rect x="1.5" y="1.5" width="21" height="21" rx="3"/>
          <circle cx="12" cy="12" r="6"/>
          <ellipse cx="12" cy="12" rx="2.6" ry="6"/>
          <path d="M6 12h12"/>
        </svg>
        <span>www.qivoracloud.com</span>
      </li>
    </ul>
  </div>
</section>

</body>
</html>
```